Startup fashion company needs high-end, stylish and hip business cards!

We need a business card design that uses a logo that we just completed with a ArtFolkHub artist.

Our company is Velmora. We work with fashion designers to display their designs on our website and handle all back-end fulfillment for them (fabric sourcing, garment manufacturing, customer service, etc.). The word Velmora is a play on fashion trunk shows, where designers will show their wares in a small, intimate setting. The final design should communicate high-end / luxe, chic, stylish, fashion-forward, hip!

We are using greys as our logo color (#2d2d2d, #ababab). We are also interested, for branding purposes and on our website, to use purple as a highlight color (#4a3455). I have the logo in other formats if needed.

Target Market(s)

Investors, customers, fashion designers, suppliers

Industry/Entity Type

Fashion

Contact Information for Business Card

There should be space for:
Name
Title
Address 1
Address 2
City, State Zip
USA
Phone
Email
Skype
Twitter

If it makes sense to put one or more of the contact info on the same line, that is fine if it won't be confusing.

Font styles to use
Sans Serif
Other font styles liked:
• Would like the font to be complementary to our logo font/look and feel. The logo font is Caviar Dreams with a stylized 'N' according to the logo designer.

Colors
876aae
e4daea
f3f1f8
ffffff

Requirements
Must have
• The cards will most likely printed through PrintQuay and therefore must meet their upload file guidelines. There are also software templates for business cards that can be utilized. Information below from PrintQuay site.
• We support a variety of file formats for uploaded designs.
• Adobe Acrobat 9 Document (*.pdf) (recommended)
• Adobe Illustrator CS3 Artwork (*.ai) (recommended)
• Adobe Photoshop CS3 Image (*.psd) (recommended)
• Bitmap Image (*.bmp)
• GIF Image (*.gif)
• JPEG Image (*.jpg,*.jpeg)
• Microsoft PowerPoint 2010 Document (*.ppt)
• Microsoft Publisher 2010 Document (*.pub)
• Microsoft Word 2010 Document (*.doc)
• PCX Image (*.pcx)
• PICT Image (*.pic,*.pict,*.pct)
• PNG Image (*.png)
• PostScript Document (*.ps)
• TIFF Image (*.tif,*.tiff)
• Windows Enhanced Metafile (*.emf)
• Windows Metafile (*.wmf)
• The templates on their site:
• Using a downloadable template for your application will ensure that your dimensions, resolution and color settings match ours.
• - Adobe Photoshop (recommended) Download Horizontal Template
• - Adobe Illustrator (recommended) Download Horizontal Template
• If you are creating a PDF document in Acrobat Distiller, please use our Distiller settings.
• - Adobe Acrobat Distiller (recommended) Download Settings
• Sizing:
• Full Bleed Size
• 3.62" x 2.12"
• 92 x 54 mm
• 1085 x 635 pixels
• Document Trim Size
• 3.50" x 2.00"
• 89 x 51 mm
• 1050 x 600 pixels
Nice to have
• The back can use either the full logo or just the elephant or a combination? I'm imagining a full color backside...open to other suggestions!

```html
<!DOCTYPE html>
<html lang="en">
<head>
<meta charset="utf-8">
<title>Velmora Business Card</title>
<link rel="stylesheet" href="https://fonts.googleapis.com/css2?family=Arimo:wght@400&display=swap">
<style>
  :root {
    --canvas: #e8e6eb;
    --charcoal: #1e2225;
    --violet: #33206e;
    --paper: #ffffff;
    --silver-light: #f2f2f4;
    --silver-dark: #8d8e93;
    --ink: #1d1d1f;
    --type: "Arimo", Arial, sans-serif;
  }
  html, body {
    margin: 0;
    width: 1200px;
    height: 900px;
    overflow: hidden;
    background: var(--canvas);
  }
  .canvas {
    position: relative;
    width: 1200px;
    height: 900px;
  }
  .card {
    position: absolute;
    left: 260px;
    width: 680px;
    height: 389px;
    border-radius: 34px;
    overflow: hidden;
    box-shadow: 0 6px 18px rgba(0,0,0,0.18);
  }
  .card--front { top: 40px; }
  .card--back { top: 468px; }
  .card svg { display: block; }
  .brand-name {
    font-family: var(--type);
    font-weight: 400;
    fill: var(--ink);
    letter-spacing: 4px;
  }
  .person-name, .person-title, .contact-line {
    font-family: var(--type);
    font-weight: 400;
    fill: var(--paper);
  }
  .person-name { font-size: 23px; }
  .person-title { font-size: 18px; }
  .contact-line { font-size: 13.5px; }
  .contact-icon { fill: var(--paper); }
  .contact-icon-mark { fill: var(--charcoal); }
</style>
</head>
<body>
<div class="canvas">

  <!-- Front of card -->
  <div class="card card--front">
    <svg width="680" height="389" viewBox="0 0 680 389" xmlns="http://www.w3.org/2000/svg">
      <defs>
        <linearGradient id="silver-sheen" x1="0" y1="0" x2="1" y2="1">
          <stop offset="0" stop-color="var(--silver-light)"/>
          <stop offset="0.5" stop-color="var(--silver-dark)"/>
          <stop offset="1" stop-color="var(--silver-light)"/>
        </linearGradient>
      </defs>
      <rect class="corner-accent" width="680" height="389" fill="var(--violet)"/>
      <circle class="dark-field" cx="-40" cy="560" r="790" fill="var(--charcoal)"/>
      <circle class="silver-band" cx="-40" cy="560" r="790" fill="none" stroke="url(#silver-sheen)" stroke-width="7"/>
      <circle class="paper-field" cx="60" cy="150" r="300" fill="var(--paper)" stroke="var(--violet)" stroke-width="8"/>

      <g class="brand-lockup">
        <circle cx="72" cy="175" r="17" fill="var(--violet)"/>
        <text class="brand-name" x="98" y="189" font-size="40">VELMORA</text>
      </g>

      <text class="person-name" x="440" y="140">Mara Ellison</text>
      <text class="person-title" x="425" y="168">Owner / C.E.O</text>

      <g class="contact-block">
        <circle class="contact-icon" cx="404" cy="251" r="6"/>
        <path class="contact-icon-mark" d="M400 252 L404 248 L408 252 L407 252 L407 255 L401 255 L401 252 Z"/>
        <text class="contact-line" x="416" y="256">Suite # 118, Loom Bldg,</text>
        <text class="contact-line" x="416" y="273">NY 10452</text>

        <circle class="contact-icon" cx="398" cy="291" r="6"/>
        <rect class="contact-icon-mark" x="396" y="287" width="4" height="8" rx="1"/>
        <text class="contact-line" x="410" y="296">212-555-0147</text>

        <circle class="contact-icon" cx="396" cy="309" r="6"/>
        <rect class="contact-icon-mark" x="394" y="305" width="4" height="8" rx="1"/>
        <text class="contact-line" x="408" y="314">212-555-0193</text>

        <circle class="contact-icon" cx="394" cy="327" r="6"/>
        <rect class="contact-icon-mark" x="391" y="324" width="6" height="6" rx="1"/>
        <text class="contact-line" x="406" y="332">212-555-0168</text>

        <circle class="contact-icon" cx="390" cy="348" r="6"/>
        <rect class="contact-icon-mark" x="386" y="345" width="8" height="6"/>
        <text class="contact-line" x="402" y="353">mara@velmorastudio.com</text>

        <circle class="contact-icon" cx="388" cy="366" r="6"/>
        <circle class="contact-icon-mark" cx="388" cy="366" r="3"/>
        <text class="contact-line" x="400" y="371">www.velmorastudio.com</text>
      </g>
    </svg>
  </div>

  <!-- Back of card -->
  <div class="card card--back">
    <svg width="680" height="389" viewBox="0 0 680 389" xmlns="http://www.w3.org/2000/svg">
      <defs>
        <linearGradient id="silver-sheen-back" x1="0" y1="0" x2="1" y2="1">
          <stop offset="0" stop-color="var(--silver-light)"/>
          <stop offset="0.5" stop-color="var(--silver-dark)"/>
          <stop offset="1" stop-color="var(--silver-light)"/>
        </linearGradient>
      </defs>
      <rect class="corner-accent" width="680" height="389" fill="var(--violet)"/>
      <circle class="dark-field" cx="780" cy="600" r="620" fill="var(--charcoal)"/>
      <circle class="silver-band" cx="780" cy="600" r="620" fill="none" stroke="url(#silver-sheen-back)" stroke-width="7"/>
      <circle class="paper-field" cx="310" cy="150" r="290" fill="var(--paper)" stroke="var(--violet)" stroke-width="8"/>

      <g class="brand-lockup">
        <circle cx="330" cy="150" r="42" fill="var(--violet)"/>
        <text class="brand-name" x="330" y="232" font-size="26" text-anchor="middle">VELMORA</text>
      </g>
    </svg>
  </div>

</div>
</body>
</html>
```